image or html template for an Email Sales Campaign – offer for a One-off Press Release

We need a design for an email promotion we are sending to existing and potential clients. We are an international digital PR platform service called Quill Harbor. See www.quillharbor-demo.com

With this email promotion we would like to push our "Single Dispatch" service. With this service a client can purchase the ability to send a press release to our database of 4800 journalists. These journalists registered to our site are from publications such as Vesta, Nest Notes, Weekend Ledger Flair, Tan Journal, Mira Interiors, Morning Bugle, KV, Zing! Journal and many others. We will be offering a special price for the service, £30 instead of £45. It will be a one off fee, with no further commitment.

With this release the client will be able to:
-upload up to 8 images to accompany their release
-personalise the release by adding their companies logo
-add caption information and stockist details to each image so that journalists have everything they need to feature their products
-email it directly to journalist's inbox's
-add their own list of contacts to be emailed too
-their press release will also be added to our release page for journalists to access 24/7

See more on information on the service here: http://www.quillharbor-demo.com/services/clients/sendquill.php?tid=1

The image we would like designed to send out as part of an email needs to take up around 1/3 of the space of a typical email. It needs to be clean and simple but fun, modern and eye catching. With graphics that are engaging but fit with our site's aesthetic. We can use images from the site (clients products) if this works. There is a deadline for the offer. This doesn't have to be HTML just a good "image", which contains products/banners/information etc, we can put in as the main part of the email

Email marketing we have previously sent:
http://clipvault-demo.com/t/qp42Rx7m
http://clipvault-demo.com/t/8h2wNoz5kLpe
http://clipvault-demo.com/t/vrTQab9x

Email marketing we like:
http://clipvault-demo.com/t/kM4fYd2hWo
http://clipvault-demo.com/t/PxRtu71bNa
http://clipvault-demo.com/t/HcweQm5z
http://clipvault-demo.com/t/9fjjkxnaBR

Target Market(s)

Interiors and Gifts companies/online retailers

Industry/Entity Type

Marketing

Requirements
Must have
• Must be modern and fun
Must convey or complement some of the key elements of the service being offered
Must be bright
Must show the offered price or highlight the discount/saving

```html
<!DOCTYPE html>
<html lang="en">
<head>
<meta charset="utf-8">
<title>Quill Harbor – Single Dispatch Offer</title>
<link rel="stylesheet" href="https://fonts.googleapis.com/css2?family=Roboto+Condensed:wght@700&family=Open+Sans:wght@400&family=Arimo:wght@400;700&family=Baloo+2:wght@700&family=Ubuntu:wght@700&display=swap">
<style>
  :root {
    --purple: #7a2f86;
    --purple-band: rgba(118, 48, 128, 0.88);
    --lime: #b7d334;
    --sky: #1aa3de;
    --white: #ffffff;
    --header-bg: #eeeef0;
    --photo-light: #e6e6e6;
    --photo-mid: #b9b9b9;
    --photo-dark: #8e8e8e;
    --strip: #6d6d6f;
    --panel: #d9d9dd;
    --ink: #3b3b3d;
    --logo-grey: #8b8b8d;
  }
  * { margin: 0; padding: 0; box-sizing: border-box; }
  html, body { width: 1200px; height: 1182px; overflow: hidden; background: var(--white); }
  .promo { position: relative; width: 1200px; height: 1182px; overflow: hidden; }

  .top-rule { position: absolute; left: 0; top: 0; width: 100%; height: 5px; background: var(--purple); }
  .masthead {
    position: absolute; left: 0; top: 5px; width: 100%; height: 125px;
    background: linear-gradient(90deg, #e2e2e4, var(--header-bg) 30%, var(--header-bg) 70%, #e2e2e4);
  }
  .brand {
    position: absolute; left: 0; top: 5px; width: 100%; height: 125px;
    display: flex; align-items: center; justify-content: center;
    font-family: "Open Sans", sans-serif; font-weight: 400; font-size: 56px;
    color: var(--logo-grey); letter-spacing: 1px;
  }
  .masthead-rule { position: absolute; left: 0; top: 130px; width: 100%; height: 8px; background: var(--purple); }

  .room-photo {
    position: absolute; left: 0; top: 138px; width: 100%; height: 562px;
    background: radial-gradient(ellipse at 55% 60%, var(--photo-light) 0%, var(--photo-mid) 55%, var(--photo-dark) 100%);
  }

  .ribbon {
    position: absolute; color: var(--white);
    font-family: "Roboto Condensed", sans-serif; font-weight: 700;
    text-transform: uppercase; display: flex; align-items: center; white-space: nowrap;
  }
  .ribbon--title {
    left: -20px; top: 165px; width: 880px; height: 125px;
    background: var(--lime); transform: rotate(-3deg);
    font-size: 88px; padding-left: 60px;
  }
  .ribbon--price {
    left: 84px; top: 278px; width: 866px; height: 118px;
    background: var(--sky); transform: rotate(-3deg);
    font-size: 60px; padding-left: 34px;
  }

  .pitch {
    position: absolute; left: 0; top: 451px; width: 100%; height: 183px;
    background: var(--purple-band);
    display: flex; align-items: center; justify-content: center;
  }
  .pitch-text {
    color: var(--white); text-align: center;
    font-family: "Arimo", sans-serif; font-weight: 400; font-size: 41px; line-height: 53px;
  }
  .pitch-text strong { font-weight: 700; }

  .benefits-heading {
    position: absolute; left: 0; top: 691px; width: 100%; height: 76px;
    background: var(--strip); color: var(--lime);
    font-family: "Baloo 2", sans-serif; font-weight: 700; font-size: 55px; line-height: 1;
    display: flex; align-items: center; justify-content: center; white-space: nowrap;
    padding-top: 6px;
  }

  .benefits {
    position: absolute; left: 0; top: 767px; width: 100%; height: 415px;
    background: var(--panel);
  }
  .benefit {
    position: absolute; width: 460px;
    font-family: "Ubuntu", sans-serif; font-weight: 700; font-size: 24px; line-height: 33px;
    color: var(--ink);
  }
  .benefit svg { position: absolute; left: -100px; top: 4px; width: 66px; height: 60px; }
  .col-left { left: 135px; }
  .col-right { left: 745px; }
</style>
</head>
<body>
<main class="promo">
  <div class="top-rule"></div>
  <div class="masthead" role="img" aria-label="Soft floral ornament pattern behind the brand name"></div>
  <div class="brand">Quill Harbor</div>
  <div class="masthead-rule"></div>

  <div class="room-photo" role="img" aria-label="Blurred photograph of a bright bedroom interior"></div>

  <div class="ribbon ribbon--title">Single Dispatch!</div>
  <div class="ribbon ribbon--price">Upgrade now just for £30</div>

  <div class="pitch">
    <p class="pitch-text">It will allow <strong>you</strong> to purchase<br>the ability to send a press release<br>to our database of <strong>4800</strong> journalists.</p>
  </div>

  <h2 class="benefits-heading">Pay just ONCE and enjoy the following benefits:</h2>

  <section class="benefits">
    <div class="benefit col-left" style="top:40px">
      <svg viewBox="0 0 66 60"><path d="M4 32 L22 50 L62 6" fill="none" stroke="var(--sky)" stroke-width="12" stroke-linecap="round" stroke-linejoin="round"/></svg>
      Upload up to 8 images<br>to accompany your release.
    </div>
    <div class="benefit col-left" style="top:123px">
      <svg viewBox="0 0 66 60"><path d="M4 32 L22 50 L62 6" fill="none" stroke="var(--sky)" stroke-width="12" stroke-linecap="round" stroke-linejoin="round"/></svg>
      Personalise the release by<br>adding your company's logo.
    </div>
    <div class="benefit col-left" style="top:213px">
      <svg viewBox="0 0 66 60"><path d="M4 32 L22 50 L62 6" fill="none" stroke="var(--sky)" stroke-width="12" stroke-linecap="round" stroke-linejoin="round"/></svg>
      Add caption information and<br>stockist details to each image<br>so that journalists have<br>everything they need<br>to feature your products.
    </div>

    <div class="benefit col-right" style="top:40px">
      <svg viewBox="0 0 66 60"><path d="M4 32 L22 50 L62 6" fill="none" stroke="var(--sky)" stroke-width="12" stroke-linecap="round" stroke-linejoin="round"/></svg>
      E-mail your release directly to<br>journalist's inbox's.
    </div>
    <div class="benefit col-right" style="top:123px">
      <svg viewBox="0 0 66 60"><path d="M4 32 L22 50 L62 6" fill="none" stroke="var(--sky)" stroke-width="12" stroke-linecap="round" stroke-linejoin="round"/></svg>
      Add your own list of contacts<br>to be e-mailed.
    </div>
    <div class="benefit col-right" style="top:213px">
      <svg viewBox="0 0 66 60"><path d="M4 32 L22 50 L62 6" fill="none" stroke="var(--sky)" stroke-width="12" stroke-linecap="round" stroke-linejoin="round"/></svg>
      Have your press release added<br>to our release page for<br>journalists to access 24/7.
    </div>
  </section>
</main>
</body>
</html>
```